2 Page Business Flyer for Finance Business

Need a two page flyer created for a finance business. Lots of text and needs to fit on two pages.

Corporate business/banking look and feel. Not too many large images. Lots of white space, clean design. Attached is color palette and the text contents of the flyer.

```html
<!DOCTYPE html>
<html lang="en">
<head>
<meta charset="utf-8">
<title>Vanilla Option Flyer</title>
<link href="https://fonts.googleapis.com/css2?family=Montserrat:wght@400;600;700&family=Oswald:wght@500;600&display=swap" rel="stylesheet">
<style>
  :root {
    --blue: #0a7fc4;
    --ink: #2b2b2b;
    --charcoal: #3d3d3e;
    --paper: #ffffff;
    --backdrop: #e6e7e9;
    --photo-dark: #5d6166;
    --photo-light: #c9cccf;
  }
  * { margin: 0; padding: 0; box-sizing: border-box; }
  html, body { width: 1200px; height: 986px; overflow: hidden; }
  body { background: var(--backdrop); font-family: "Montserrat", sans-serif; color: var(--ink); }
  .flyer {
    position: absolute; left: 240px; top: 23px; width: 720px; height: 940px;
    background: var(--paper); overflow: hidden; box-shadow: 0 6px 24px rgba(0,0,0,.15);
  }
  .header-art { position: absolute; left: 0; top: 0; }
  .intro-panel {
    position: absolute; left: 30px; top: 24px; width: 210px; height: 318px;
    background: var(--blue); color: var(--paper); padding: 22px 18px;
  }
  .brand {
    background: var(--paper); color: var(--blue); font-family: "Oswald", sans-serif;
    font-weight: 600; font-size: 22px; padding: 8px 14px; margin-bottom: 20px; letter-spacing: .5px;
  }
  .intro-title { font-family: "Oswald", sans-serif; font-weight: 500; font-size: 17px; line-height: 1.15; text-transform: uppercase; margin-bottom: 12px; }
  .intro-text { font-size: 9.2px; line-height: 1.45; }
  .column { position: absolute; font-size: 10.6px; line-height: 1.42; }
  .column p { margin-bottom: 14px; text-align: justify; }
  .col-left { left: 36px; top: 362px; width: 310px; }
  .col-right { left: 384px; top: 312px; width: 300px; font-size: 9.8px; }
  .steps { list-style: none; margin: 4px 0 16px; }
  .steps li { position: relative; padding-left: 20px; margin-bottom: 8px; }
  .steps svg { position: absolute; left: 0; top: 2px; }
  .example-title { color: var(--blue); font-weight: 700; font-size: 13px; text-transform: uppercase; margin-top: 6px; }
  .example-sub { font-weight: 700; font-size: 12.5px; text-transform: uppercase; margin-bottom: 12px; }
  .portrait { position: absolute; left: 430px; top: 560px; }
  .footer-art { position: absolute; left: 0; top: 760px; }
  .call { position: absolute; left: 40px; top: 876px; color: var(--paper); }
  .call-label { font-size: 20px; line-height: 1.2; }
  .call-number { font-size: 22px; font-weight: 700; letter-spacing: 1px; line-height: 1.2; }
  .contact {
    position: absolute; top: 852px; color: var(--paper); font-size: 10.5px;
    display: flex; align-items: center; gap: 7px; white-space: nowrap;
  }
  .contact-web { left: 400px; }
  .contact-mail { left: 566px; }
</style>
</head>
<body>
<main class="flyer">
  <svg class="header-art" width="720" height="360" viewBox="0 0 720 360">
    <path d="M0 40 Q360 -10 720 40" fill="none" stroke="var(--charcoal)" stroke-width="5"/>
    <defs>
      <linearGradient id="meetingTones" x1="0" y1="0" x2="1" y2="1">
        <stop offset="0" stop-color="var(--photo-light)"/>
        <stop offset="0.6" stop-color="#9aa0a6"/>
        <stop offset="1" stop-color="var(--photo-dark)"/>
      </linearGradient>
    </defs>
    <path role="img" aria-label="Photo of businessmen talking at a meeting table"
          d="M0 52 Q360 8 720 52 L720 240 Q360 330 0 300 Z" fill="url(#meetingTones)"/>
  </svg>

  <section class="intro-panel">
    <div class="brand">Meridian FX</div>
    <h1 class="intro-title">How does a vanilla option contract work?</h1>
    <p class="intro-text">The buyer of a vanilla option receives protection against an adverse movement in the exchange rate while allowing full participation in a beneficial move. At no time is the buyer of a Vanilla Option obligated to exercise the Option and transact the currencies, therefore providing flexibility in cases where the requirement to purchase foreign currency is not certain.</p>
  </section>

  <section class="column col-left">
    <p>A buyer of vanilla options is required to pay a premium (like an insurance premium) for the right, but not the obligation, to exchange currency at a predetermined rate on a predetermined date.</p>
    <ul class="steps">
      <li><svg width="11" height="11" viewBox="0 0 11 11"><circle cx="5.5" cy="5.5" r="5.5" fill="var(--blue)"/><path d="M3 5.6l1.8 1.8L8 4" stroke="#fff" stroke-width="1.4" fill="none"/></svg>Set a protection rate which will be your worst-case scenario at expiry</li>
      <li><svg width="11" height="11" viewBox="0 0 11 11"><circle cx="5.5" cy="5.5" r="5.5" fill="var(--blue)"/><path d="M3 5.6l1.8 1.8L8 4" stroke="#fff" stroke-width="1.4" fill="none"/></svg>Determine the amount of currency you wish to protect</li>
      <li><svg width="11" height="11" viewBox="0 0 11 11"><circle cx="5.5" cy="5.5" r="5.5" fill="var(--blue)"/><path d="M3 5.6l1.8 1.8L8 4" stroke="#fff" stroke-width="1.4" fill="none"/></svg>Choose an expiry date for the contract</li>
      <li><svg width="11" height="11" viewBox="0 0 11 11"><circle cx="5.5" cy="5.5" r="5.5" fill="var(--blue)"/><path d="M3 5.6l1.8 1.8L8 4" stroke="#fff" stroke-width="1.4" fill="none"/></svg>Calculate the premium you are required to pay</li>
    </ul>
    <h2 class="example-title">Let's look at an example:</h2>
    <h3 class="example-sub">You are in importer.</h3>
    <p>Your construction company has bid on a project that if successful, will require you to import materials from the United States to use in construction. You have used todays pricing of materials in calculating your bid and want to protect against an adverse move in the US dollar exchange rate from eroding your margin if your bid is chosen for the project.</p>
    <p>You choose to buy a Vanilla Call which will protect you from a rise in the USD/CAD exchange rate above your protection rate. You choose to buy protection on $500,000 USD, with a protection rate (strike rate) of 1.3300 expiring 3 months from now. You are required to pay a premium which in this case is calculated to be 1.8%, or 11,970 CAD.</p>
  </section>

  <section class="column col-right">
    <p>Your bid is successful: If the exchange rate is below your protection rate at expiration, you have no obligation relating to the vanilla call and you are free to buy USD at the cheaper spot rate. If the exchange rate is above your protection rate, your have the right to purchase your USD at the protection rate, and thereby claiming your insurance policy.</p>
    <p>Your bid is not successful: You have no obligation relating to the vanilla option however, if at expiry the exchange rate is above the protection rate, you may exercise your right to buy USD at the lower rate and simultaneous sell USD back at the prevailing spot rate, thereby recouping some or all of the premium paid to buy the option. Alternatively, if you find out your bid was not successful with time still left until expiration, you may sell your option back into the market in the case that it still has residual value, which will depend on various market factors.</p>
  </section>

  <svg class="portrait" width="290" height="260" viewBox="0 0 290 260" role="img" aria-label="Photo of a smiling businesswoman in an office">
    <defs>
      <linearGradient id="officeTones" x1="0" y1="0" x2="1" y2="0">
        <stop offset="0" stop-color="#4a4440"/>
        <stop offset="0.5" stop-color="#8c8a84"/>
        <stop offset="1" stop-color="#d9dcd8"/>
      </linearGradient>
    </defs>
    <rect width="290" height="260" fill="url(#officeTones)"/>
  </svg>

  <svg class="footer-art" width="720" height="180" viewBox="0 0 720 180">
    <polygon points="0,108 370,96 362,180 0,180" fill="var(--blue)"/>
    <polygon points="382,68 720,40 720,180 372,180" fill="var(--charcoal)"/>
  </svg>

  <div class="call">
    <div class="call-label">Call Us</div>
    <div class="call-number">555 014 2290</div>
  </div>
  <div class="contact contact-web">
    <svg width="14" height="14" viewBox="0 0 14 14"><circle cx="7" cy="7" r="6" fill="none" stroke="#fff" stroke-width="1.4"/><path d="M1 7h12M7 1c-3 3.5-3 8.5 0 12M7 1c3 3.5 3 8.5 0 12" stroke="#fff" stroke-width="1" fill="none"/></svg>
    www.meridianfx.com
  </div>
  <div class="contact contact-mail">
    <svg width="16" height="12" viewBox="0 0 16 12"><rect x="0.7" y="0.7" width="14.6" height="10.6" fill="none" stroke="#fff" stroke-width="1.4"/><path d="M1 1l7 6 7-6" stroke="#fff" stroke-width="1.4" fill="none"/></svg>
    info@meridianfx.com
  </div>
</main>
</body>
</html>
```